Flyer Project for Industrial Company

We need to change an old flyer and update with new information. Could have some updated design elements! Like the second page design. Keep the text the same. I have added some photos that we would like to use and have more.
We would like it to be professional, it is going out in a direct mail so we need it to be eye catching.
Target Market(s)
General Contracors
Industry/Entity Type
industrial services
Font styles to use
Serif
Sans Serif
Colors
EB3D1F
EC4F4E
F09395
F8D3D4
FCEDEE
Requirements
Must have
- Updated design and modern elements

```html
<!DOCTYPE html>
<html lang="en">
<head>
<meta charset="utf-8">
<title>Northfield Companies – Flyer</title>
<link rel="stylesheet" href="https://fonts.googleapis.com/css2?family=Roboto+Slab:wght@700;800&family=Open+Sans:wght@400;600;700&display=swap">
<style>
:root{
  --red:#EB3D1F;
  --red-soft:#EC4F4E;
  --pink:#F09395;
  --blush:#F8D3D4;
  --mist:#FCEDEE;
  --ink:#1f1f22;
  --charcoal:#2b2b2f;
  --paper:#ffffff;
  --stage:#e4e4e4;
  --photo-site:linear-gradient(160deg,#8b8a80 0%,#6e6a5c 45%,#a39a84 100%);
  --photo-silo:linear-gradient(180deg,#7fa6cf 0%,#b9c4cc 45%,#8d8d88 100%);
  --photo-machine:linear-gradient(150deg,#c9a33a 0%,#7d7566 60%,#5a5850 100%);
}
*{box-sizing:border-box;margin:0;padding:0}
html,body{width:800px;height:1200px;overflow:hidden}
body{background:var(--stage);font-family:"Open Sans",Arial,sans-serif;color:var(--ink);position:relative}
.page{position:absolute;left:172px;width:456px;height:590px;background:var(--paper);overflow:hidden;box-shadow:0 2px 6px rgba(0,0,0,.18)}
.page--one{top:5px}
.page--two{top:605px}
.photo{position:absolute}
.brand{position:absolute;top:12px;left:14px;color:#fff;font-family:"Open Sans",Arial,sans-serif;font-weight:700;font-size:11px;letter-spacing:.3px;display:flex;align-items:center;gap:6px;z-index:2}
.brand i{width:8px;height:8px;background:var(--red);display:block}
.heading{font-family:"Roboto Slab",Georgia,serif;font-weight:800;text-transform:uppercase;letter-spacing:.4px}
.band{position:absolute;left:0;width:100%;display:flex;align-items:center;justify-content:center}
.band--red{background:var(--red);color:#fff}
.band--dark{background:var(--charcoal);color:#fff}
.body-copy{position:absolute;font-size:6.4px;line-height:1.55;color:#333;text-align:center}
.col-head{background:var(--charcoal);color:#fff;font-family:"Roboto Slab",Georgia,serif;font-weight:700;font-size:8.5px;padding:5px 8px;margin-bottom:6px}
.service-list{list-style:none}
.service-list li{display:flex;align-items:center;gap:6px;font-size:6.8px;padding:5.2px 0;border-bottom:1px solid var(--blush)}
.service-list svg{flex:none}
.expertise-grid{display:grid;grid-template-columns:repeat(3,1fr);gap:6px}
.expertise-grid figure{font-size:5.6px;text-align:center;color:#333}
.expertise-grid .thumb{height:52px;margin-bottom:3px}
.tagline{font-family:"Roboto Slab",Georgia,serif;font-weight:800;font-size:15px;color:#fff;letter-spacing:.5px}
.thumbs-strip{position:absolute;left:0;width:100%;background:var(--red);padding:6px 18px;display:flex;gap:6px}
.thumbs-strip .thumb{flex:1;height:44px;border:2px solid #fff}
.partnership{position:absolute;left:0;width:100%;background:var(--charcoal);padding:10px 18px}
.stats{display:grid;grid-template-columns:repeat(3,1fr);gap:8px;margin-top:8px}
.stat{background:var(--mist);border-top:3px solid var(--red);padding:6px;text-align:center}
.stat b{display:block;font-family:"Roboto Slab",Georgia,serif;font-size:13px;color:var(--red)}
.stat span{font-size:5.6px;line-height:1.4;color:#333;display:block}
.contact-row{position:absolute;bottom:0;left:0;width:100%;height:40px;background:var(--charcoal);display:flex;justify-content:space-around;align-items:center;color:#fff;font-size:7px;font-weight:600}
.contact-row span{display:flex;align-items:center;gap:5px}
</style>
</head>
<body>

<section class="page page--one">
  <div class="brand"><i></i>Northfield Companies</div>
  <div class="photo" style="top:0;left:0;width:456px;height:196px;background:var(--photo-site)" role="img" aria-label="Aerial view of a demolition site with excavators"></div>
  <div class="band band--dark" style="top:196px;height:24px"><h2 class="heading" style="font-size:11px;color:#fff">The <span style="color:var(--pink)">Industry</span> Leader</h2></div>
  <p class="body-copy" style="top:230px;left:26px;width:404px">Northfield Companies is a leading provider of demolition, environmental and site services across the country. For more than six decades our crews have delivered safe, efficient results for contractors, owners and public agencies, backed by our own fleet of heavy equipment and experienced people.</p>
  <p class="body-copy" style="top:268px;left:26px;width:404px;font-weight:700;color:var(--red)">We are proud to be the partner contractors call first.</p>

  <div style="position:absolute;top:290px;left:18px;width:180px">
    <h3 class="col-head">Our Services Include:</h3>
    <ul class="service-list">
      <li><svg width="9" height="9" viewBox="0 0 9 9"><rect width="9" height="9" fill="#EB3D1F"/><path d="M2 4.6l1.7 1.7L7 3" stroke="#fff" stroke-width="1.3" fill="none"/></svg>Emergency Response</li>
      <li><svg width="9" height="9" viewBox="0 0 9 9"><rect width="9" height="9" fill="#EB3D1F"/><path d="M2 4.6l1.7 1.7L7 3" stroke="#fff" stroke-width="1.3" fill="none"/></svg>Commercial and Industrial Demolition</li>
      <li><svg width="9" height="9" viewBox="0 0 9 9"><rect width="9" height="9" fill="#EB3D1F"/><path d="M2 4.6l1.7 1.7L7 3" stroke="#fff" stroke-width="1.3" fill="none"/></svg>Environmental Services</li>
      <li><svg width="9" height="9" viewBox="0 0 9 9"><rect width="9" height="9" fill="#EB3D1F"/><path d="M2 4.6l1.7 1.7L7 3" stroke="#fff" stroke-width="1.3" fill="none"/></svg>Grading, Excavation and Infrastructure</li>
      <li><svg width="9" height="9" viewBox="0 0 9 9"><rect width="9" height="9" fill="#EB3D1F"/><path d="M2 4.6l1.7 1.7L7 3" stroke="#fff" stroke-width="1.3" fill="none"/></svg>Materials Reclamation</li>
      <li><svg width="9" height="9" viewBox="0 0 9 9"><rect width="9" height="9" fill="#EB3D1F"/><path d="M2 4.6l1.7 1.7L7 3" stroke="#fff" stroke-width="1.3" fill="none"/></svg>Rigging, Machinery Moving Equipment</li>
      <li><svg width="9" height="9" viewBox="0 0 9 9"><rect width="9" height="9" fill="#EB3D1F"/><path d="M2 4.6l1.7 1.7L7 3" stroke="#fff" stroke-width="1.3" fill="none"/></svg>Cranes</li>
    </ul>
  </div>

  <div style="position:absolute;top:290px;left:210px;width:228px">
    <h3 class="col-head">Our Areas of Expertise</h3>
    <div class="expertise-grid">
      <figure><div class="thumb" style="background:var(--photo-machine)" role="img" aria-label="Excavator at work"></div>Industrial Plants</figure>
      <figure><div class="thumb" style="background:var(--photo-site)" role="img" aria-label="Bridge demolition"></div>Bridges</figure>
      <figure><div class="thumb" style="background:var(--photo-silo)" role="img" aria-label="Storage silos"></div>Silos and Tanks</figure>
      <figure><div class="thumb" style="background:var(--photo-site)" role="img" aria-label="Building demolition"></div>High Rise</figure>
      <figure><div class="thumb" style="background:var(--photo-machine)" role="img" aria-label="Heavy equipment fleet"></div>Power Plants</figure>
      <figure><div class="thumb" style="background:var(--photo-silo)" role="img" aria-label="Hospital demolition"></div>Hospitals</figure>
    </div>
  </div>

  <p class="body-copy" style="top:512px;left:26px;width:404px;font-weight:600">Call us today to discuss your next project with our estimating team.</p>
  <div class="band band--red" style="bottom:0;height:48px"><p class="tagline">SHAPING AMERICA'S SKYLINE SINCE 1959.</p></div>
</section>

<section class="page page--two">
  <div class="brand"><i></i>Northfield Companies</div>
  <div class="photo" style="top:0;left:0;width:456px;height:196px;background:var(--photo-silo)" role="img" aria-label="Crane dismantling industrial silos"></div>
  <div class="band band--red" style="top:196px;height:24px"><h2 class="heading" style="font-size:11px">Why Choose Northfield?</h2></div>
  <p class="body-copy" style="top:228px;left:26px;width:404px">Our safety record, in-house equipment and seasoned project managers let us move quickly and keep schedules on track. We handle permits, abatement, demolition and recycling under one contract, so general contractors have a single accountable partner from start to finish.</p>
  <div class="thumbs-strip" style="top:266px">
    <div class="thumb" style="background:var(--photo-machine)" role="img" aria-label="Crane on site"></div>
    <div class="thumb" style="background:var(--photo-site)" role="img" aria-label="Demolition debris"></div>
    <div class="thumb" style="background:var(--photo-silo)" role="img" aria-label="Industrial structure"></div>
    <div class="thumb" style="background:var(--photo-machine)" role="img" aria-label="Excavator fleet"></div>
  </div>
  <div class="partnership" style="top:326px">
    <h3 class="heading" style="text-align:center;font-size:12px;color:#fff">A 20 Year Partnership</h3>
    <div class="stats">
      <div class="stat"><b>20+</b><span>Years working side by side with leading builders.</span></div>
      <div class="stat"><b>500+</b><span>Projects finished safely, on time and on budget.</span></div>
      <div class="stat"><b>24/7</b><span>Emergency crews ready to respond any day of the year.</span></div>
    </div>
  </div>
  <p class="body-copy" style="top:436px;left:26px;width:404px">From first walk-through to final clean site, our team brings the planning, people and machines to deliver results you can count on.</p>
  <div class="band band--red" style="top:466px;height:26px"><h2 class="heading" style="font-size:10px">Ready to learn more about partnering with us?</h2></div>
  <p class="body-copy" style="top:506px;left:26px;width:404px;font-weight:600">Contact our team for a project consultation or estimate.</p>
  <div class="contact-row">
    <span><svg width="9" height="9" viewBox="0 0 10 10"><path d="M2 1h2l1 2.5-1.3.8a6 6 0 0 0 2 2l.8-1.3L9 6v2a1 1 0 0 1-1 1A7 7 0 0 1 1 2a1 1 0 0 1 1-1z" fill="#EC4F4E"/></svg>555-010-2468</span>
    <span><svg width="10" height="8" viewBox="0 0 10 8"><rect x=".5" y=".5" width="9" height="7" fill="none" stroke="#EC4F4E"/><path d="M.5.5L5 4.5 9.5.5" fill="none" stroke="#EC4F4E"/></svg>info@northfield.example</span>
    <span><svg width="8" height="10" viewBox="0 0 8 10"><path d="M4 0a4 4 0 0 1 4 4c0 3-4 6-4 6S0 7 0 4a4 4 0 0 1 4-4z" fill="#EC4F4E"/><circle cx="4" cy="4" r="1.4" fill="#2b2b2f"/></svg>northfield.example</span>
  </div>
</section>

</body>
</html>
```